Business Card Design Project

I have attached the logo and the colour pallete for the branding for the company.

Creative designs for business cards are needed.

The Company is modern corporate.

Industry/Entity Type

Business

```html
<!DOCTYPE html>
<html lang="en">
<head>
<meta charset="utf-8">
<title>Stepwise Business Cards</title>
<link rel="stylesheet" href="https://fonts.googleapis.com/css2?family=Didact+Gothic&display=swap">
<style>
  :root {
    --backdrop: #e4e5e7;
    --paper: #ffffff;
    --orange-light: #f3922a;
    --orange-deep: #e8552b;
    --ink: #2b2320;
    --card-shadow: rgba(0, 0, 0, 0.22);
  }
  * { margin: 0; padding: 0; box-sizing: border-box; }
  html, body {
    width: 1200px;
    height: 968px;
    overflow: hidden;
    background: var(--backdrop);
    font-family: "Didact Gothic", sans-serif;
  }
  .sheet {
    position: relative;
    width: 1200px;
    height: 968px;
  }
  .card {
    position: absolute;
    left: 250px;
    width: 700px;
    height: 400px;
    border-radius: 4px;
    overflow: hidden;
    box-shadow: 0 10px 28px var(--card-shadow);
  }
  .card-orange-field {
    background: radial-gradient(ellipse at 50% 45%, var(--orange-light) 0%, var(--orange-deep) 85%);
  }

  /* Front */
  .card-front { top: 56px; background: var(--paper); }
  .card-front .lower-band {
    position: absolute;
    left: 0; right: 0; bottom: 0;
    height: 240px;
  }
  .card-front .brand-name {
    position: absolute;
    left: 150px;
    top: 106px;
    font-size: 92px;
    line-height: 1;
    color: var(--ink);
    letter-spacing: -1px;
  }
  .card-front .holder-name {
    position: absolute;
    right: 96px;
    top: 222px;
    font-size: 34px;
    color: var(--ink);
  }
  .card-front .contact {
    position: absolute;
    left: 40px;
    bottom: 42px;
    font-size: 20px;
    line-height: 1.25;
    color: var(--ink);
    list-style: none;
  }

  /* Back */
  .card-back { top: 512px; }
  .card-back .brand-name {
    position: absolute;
    left: 90px;
    top: 150px;
    font-size: 84px;
    line-height: 1;
    color: var(--paper);
    letter-spacing: -1px;
  }
</style>
</head>
<body>
  <main class="sheet">
    <section class="card card-front" aria-label="Business card front">
      <div class="lower-band card-orange-field"></div>
      <div class="brand-name">stepwise</div>
      <p class="holder-name">Daniel Reyes</p>
      <ul class="contact">
        <li>danielreyes@stepwisehub.com</li>
        <li>www.stepwisehub.com</li>
      </ul>
    </section>

    <section class="card card-back card-orange-field" aria-label="Business card back">
      <div class="brand-name">stepwise</div>
    </section>
  </main>
</body>
</html>
```